International Consultancy Needs Slick Professional Presentation Graphic

Quarvel are an international engineering and advisory consultancy servicing the mining industry with a mix of Technology (Software), Services (consulting) and Systems (work structures).

We need a slick presentation graphic for use in presentation slides, whitepapers. I have attached a basic pic of the information we want to convey. Flat or 3D no preference, colouring no preference. Don't have to be circles, that was just easiest to draft up initially.

Industry/Entity Type

Mining

```html
<!DOCTYPE html>
<html lang="en">
<head>
<meta charset="utf-8">
<title>Quarvel Capability Model</title>
<link rel="stylesheet" href="https://fonts.googleapis.com/css2?family=Montserrat:wght@700;800&family=Oswald:wght@500&display=swap">
<style>
  :root {
    --page: #f4f5f5;
    --ink: #1f2a2e;
    --tech-light: #d6348a;
    --tech-dark: #a51d68;
    --serv-light: #f5dc1c;
    --serv-dark: #ec9322;
    --sys-light: #1e9ad8;
    --sys-dark: #1478b8;
    --overlap-ts: #93bd2c;
    --overlap-tsy: #d8a2aa;
    --overlap-ssy: #9a4985;
    --core-light: #5e5e60;
    --core-dark: #2c2c2e;
    --core-text: #a9dcf3;
    --label: #ffffff;
    --leader: #2b3336;
  }
  html, body {
    margin: 0;
    padding: 0;
    overflow: hidden;
    background: var(--page);
  }
  .canvas {
    position: relative;
    width: 1200px;
    height: 990px;
    overflow: hidden;
    background: radial-gradient(ellipse at 50% 45%, #ffffff 0%, var(--page) 75%);
  }
  .diagram {
    position: absolute;
    inset: 0;
  }
  .callout {
    position: absolute;
    margin: 0;
    font-family: "Montserrat", sans-serif;
    font-weight: 700;
    font-size: 27px;
    line-height: 36px;
    letter-spacing: 0.5px;
    color: var(--ink);
    text-align: center;
    width: 400px;
  }
  .callout--top { left: 390px; top: 82px; }
  .callout--left { left: 22px; top: 817px; }
  .callout--right { left: 769px; top: 817px; }
  .ring-label {
    font-family: "Montserrat", sans-serif;
    font-weight: 800;
    font-size: 29px;
    letter-spacing: 2px;
    fill: var(--label);
  }
  .core-label {
    font-family: "Oswald", sans-serif;
    font-weight: 500;
    font-size: 36px;
    fill: var(--core-text);
  }
  .leader {
    fill: none;
    stroke: var(--leader);
    stroke-width: 2.5;
    stroke-dasharray: 2 4;
  }
  .node {
    fill: var(--leader);
    stroke: #ffffff;
    stroke-width: 3;
  }
  .icon-light { fill: #ffffff; }
  .icon-dark { fill: #1f2a2e; }
</style>
</head>
<body>
<div class="canvas">
  <svg class="diagram" width="1200" height="990" viewBox="0 0 1200 990" xmlns="http://www.w3.org/2000/svg">
    <defs>
      <radialGradient id="grad-tech" cx="55%" cy="55%" r="60%">
        <stop offset="0" stop-color="var(--tech-light)"/>
        <stop offset="1" stop-color="var(--tech-dark)"/>
      </radialGradient>
      <radialGradient id="grad-serv" cx="40%" cy="55%" r="65%">
        <stop offset="0" stop-color="var(--serv-light)"/>
        <stop offset="1" stop-color="var(--serv-dark)"/>
      </radialGradient>
      <radialGradient id="grad-sys" cx="50%" cy="35%" r="65%">
        <stop offset="0" stop-color="var(--sys-light)"/>
        <stop offset="1" stop-color="var(--sys-dark)"/>
      </radialGradient>
      <radialGradient id="grad-core" cx="50%" cy="40%" r="55%">
        <stop offset="0" stop-color="var(--core-light)"/>
        <stop offset="1" stop-color="var(--core-dark)"/>
      </radialGradient>
      <filter id="soft-shadow" x="-20%" y="-20%" width="140%" height="140%">
        <feDropShadow dx="0" dy="8" stdDeviation="10" flood-color="#000" flood-opacity="0.22"/>
      </filter>
      <clipPath id="clip-tech"><circle cx="460" cy="435" r="228"/></clipPath>
      <clipPath id="clip-serv"><circle cx="712" cy="435" r="228"/></clipPath>
      <path id="arc-tech" d="M276 451 A185 185 0 0 1 538 267"/>
      <path id="arc-serv" d="M790 267 A185 185 0 0 1 880 513"/>
      <path id="arc-sys" d="M458 798 A200 200 0 0 0 716 798"/>
    </defs>

    <g class="rings" filter="url(#soft-shadow)">
      <circle cx="587" cy="645" r="230" fill="url(#grad-sys)"/>
      <circle cx="712" cy="435" r="228" fill="url(#grad-serv)"/>
      <circle cx="460" cy="435" r="228" fill="url(#grad-tech)"/>
    </g>

    <g clip-path="url(#clip-tech)">
      <circle cx="712" cy="435" r="228" fill="var(--overlap-ts)"/>
      <circle cx="587" cy="645" r="230" fill="var(--overlap-tsy)"/>
    </g>
    <g clip-path="url(#clip-serv)">
      <circle cx="587" cy="645" r="230" fill="var(--overlap-ssy)"/>
    </g>
    <g clip-path="url(#clip-tech)">
      <g clip-path="url(#clip-serv)">
        <circle cx="587" cy="645" r="230" fill="url(#grad-core)"/>
      </g>
    </g>

    <text class="ring-label"><textPath href="#arc-tech" startOffset="50%" text-anchor="middle">TECHNOLOGY</textPath></text>
    <text class="ring-label"><textPath href="#arc-serv" startOffset="50%" text-anchor="middle">SERVICES</textPath></text>
    <text class="ring-label"><textPath href="#arc-sys" startOffset="50%" text-anchor="middle">SYSTEMS</textPath></text>
    <text class="core-label" x="586" y="520" text-anchor="middle">CAPABILITY</text>

    <g class="icon-devices">
      <rect x="338" y="360" width="74" height="52" rx="4" class="icon-light"/>
      <rect x="345" y="367" width="60" height="38" fill="var(--tech-dark)"/>
      <rect x="367" y="412" width="16" height="12" class="icon-light"/>
      <rect x="356" y="423" width="38" height="5" rx="2" class="icon-light"/>
      <rect x="330" y="398" width="22" height="36" rx="3" class="icon-light"/>
      <rect x="334" y="403" width="14" height="25" fill="var(--tech-dark)"/>
      <rect x="398" y="396" width="32" height="40" rx="3" class="icon-light"/>
      <rect x="402" y="401" width="24" height="29" fill="var(--tech-dark)"/>
    </g>

    <g class="icon-users">
      <circle cx="757" cy="335" r="17" class="icon-light"/>
      <path d="M727 377 Q727 356 757 356 Q787 356 787 377 Z" class="icon-light"/>
      <circle cx="852" cy="425" r="17" class="icon-dark"/>
      <path d="M822 467 Q822 446 852 446 Q882 446 882 467 Z" class="icon-dark"/>
      <path d="M800 398 L822 376" stroke="var(--ink)" stroke-width="3"/>
      <path d="M813 376 L822 376 L822 385" fill="none" stroke="var(--ink)" stroke-width="3"/>
      <path d="M798 404 L820 426" stroke="#ffffff" stroke-width="3"/>
      <path d="M811 426 L820 426 L820 417" fill="none" stroke="#ffffff" stroke-width="3"/>
    </g>

    <g class="icon-gears" fill="none" stroke="#ffffff">
      <circle cx="566" cy="724" r="11" stroke-width="9" stroke-dasharray="5 3.6"/>
      <circle cx="566" cy="724" r="9" stroke-width="6"/>
      <circle cx="608" cy="762" r="22" stroke-width="14" stroke-dasharray="8 5.8"/>
      <circle cx="608" cy="762" r="18" stroke-width="12"/>
    </g>

    <path class="leader" d="M590 358 V172"/>
    <path d="M584 172 L596 172 L590 163 Z" fill="var(--leader)"/>
    <path class="leader" d="M453 585 L218 743 V796"/>
    <path d="M212 795 L224 795 L218 803 Z" fill="var(--leader)"/>
    <path class="leader" d="M730 585 L968 743 V796"/>
    <path d="M962 795 L974 795 L968 803 Z" fill="var(--leader)"/>
    <circle class="node" cx="590" cy="358" r="6"/>
    <circle class="node" cx="453" cy="585" r="6"/>
    <circle class="node" cx="730" cy="585" r="6"/>
  </svg>

  <p class="callout callout--top">USER INTERFACE<br>ENGINEERING</p>
  <p class="callout callout--left">USER INTERFACE<br>ENGINEERING</p>
  <p class="callout callout--right">ORGANISATION<br>DESIGN</p>
</div>
</body>
</html>
```